Beyond The Ledger Double Sided DL Flyer

We need a double sided flyer that we provide to a Real Estate agent for leeds. It should provide our basic services as well as a modern look and feel. The brochure should incorporate our Brand colors and have a graphic that centres around money and property. I have included a couple of pictures that we like (but have not yet purchased from PIXVAULT) as an indication of the type of picture we like.

WE need to also show the Beyond The Ledger brand and have our Phone / address's and email details.

Target Market(s)

Realestate clients (Property Investors)

Industry/Entity Type

Financial Planning

Requirements
Must have
• Picture on Front (maybe the logo on back)
• Please incorporate existing logo colours.

```html
<!DOCTYPE html>
<html lang="en">
<head>
<meta charset="utf-8">
<title>Beyond The Ledger – DL Flyer</title>
<link rel="stylesheet" href="https://fonts.googleapis.com/css2?family=Questrial&family=Lato:wght@400;700&display=swap">
<style>
  :root{
    --green:#7dc242;
    --green-dark:#5f9f2c;
    --ink:#2a2c2b;
    --panel-dark:#2b2d2c;
    --paper:#ffffff;
    --mist:#f1f2f1;
    --backdrop:#e7e8e6;
    --text:#333533;
  }
  *{box-sizing:border-box;margin:0;padding:0}
  html,body{width:1200px;height:1200px;overflow:hidden;background:var(--backdrop)}
  body{position:relative;font-family:"Lato",sans-serif;color:var(--text)}
  .flyer{position:absolute;top:176px;width:400px;height:824px;overflow:hidden;box-shadow:0 6px 18px rgba(0,0,0,.18)}
  .flyer--front{left:174px;background:linear-gradient(180deg,var(--paper) 40%,var(--mist) 85%)}
  .flyer--back{left:626px;background:var(--panel-dark)}
  .caption{position:absolute;top:1022px;width:400px;text-align:center;font-family:"Questrial",sans-serif;font-size:21px;color:#555}
  .caption--front{left:174px}.caption--back{left:626px}
  .abs{position:absolute;left:0;width:100%}
  .center{text-align:center}

  .photo{position:absolute;left:0;width:100%}
  .photo--front{top:0;height:380px;background:linear-gradient(180deg,#3f7d2a 0%,#6aa64a 45%,#a98f6c 78%,#b89e7b 100%)}
  .photo--back{top:96px;height:320px;background:linear-gradient(160deg,#b6c2c8 0%,#dfe4e2 45%,#f0efe9 80%,#e6e7e3 100%)}

  .brand{position:absolute;left:0;width:100%;display:flex;align-items:center;justify-content:center;gap:9px}
  .brand__dot{width:18px;height:18px;border-radius:50%;background:var(--green)}
  .brand__name{font-family:"Questrial",sans-serif;font-size:24px;color:var(--ink);letter-spacing:.3px}

  .headline{font-family:"Questrial",sans-serif;font-size:17.5px;color:var(--ink)}
  .headline .hl{color:var(--green-dark)}
  .subhead{font-family:"Questrial",sans-serif;font-size:15.5px;color:var(--ink);font-weight:700}
  .services{position:absolute;top:514px;left:0;width:100%;list-style:none}
  .service{height:39px;display:flex;flex-direction:column;align-items:center;font-size:12.4px;color:var(--text)}
  .service__icon{width:20px;height:20px;border-radius:50%;border:1.5px solid #6b6d6b;display:flex;align-items:center;justify-content:center;margin-bottom:2px}
  .service__icon i{width:8px;height:8px;border-radius:50%;background:var(--green)}

  .phone-line{font-family:"Questrial",sans-serif;color:#fff;display:flex;align-items:center;justify-content:center;gap:6px}
  .web{font-family:"Lato",sans-serif;color:#fff;letter-spacing:3.4px;font-size:12px}

  .advice{font-family:"Questrial",sans-serif;font-weight:700;font-size:36px;color:var(--green);letter-spacing:1px}
  .trust{font-family:"Questrial",sans-serif;font-size:35px;color:#fff}
  .lead{font-family:"Questrial",sans-serif;font-size:17.5px;color:var(--green)}
  .contact{font-family:"Questrial",sans-serif;font-size:15.5px;color:#fff;font-weight:700}
  .detail{font-size:11.8px;color:#fff;line-height:15px}
  .icon{display:block;margin:0 auto}
  .social{position:absolute;top:784px;left:22px;width:356px;display:flex;align-items:center;gap:6px}
  .social__rule{flex:1;height:1px;background:var(--green)}
  .social__dot{width:15px;height:15px;border-radius:50%;background:var(--green)}
</style>
</head>
<body>

<!-- FRONT -->
<section class="flyer flyer--front">
  <div class="photo photo--front" role="img" aria-label="Photo: hand watering a seedling in a coin-filled jar beside a small house model and stacks of coins"></div>
  <svg class="abs" style="top:300px" width="400" height="110" viewBox="0 0 400 110">
    <path d="M0,40 Q190,118 400,58 L400,110 L0,110 Z" fill="#ffffff"/>
    <path d="M0,32 Q190,110 352,66" fill="none" stroke="#7dc242" stroke-width="7"/>
    <path d="M340,50 L380,57 L350,82 Z" fill="#7dc242"/>
  </svg>

  <div class="brand" style="top:404px"><span class="brand__dot"></span><span class="brand__name">Beyond The Ledger</span></div>
  <p class="abs center headline" style="top:462px"><span class="hl">Accountants and</span> Financial Advisors</p>
  <p class="abs center subhead" style="top:488px;font-weight:400">Who specialise in:</p>

  <ul class="services">
    <li class="service"><span class="service__icon"><i></i></span>Negative Gearing &amp; Investment Properties</li>
    <li class="service"><span class="service__icon"><i></i></span>Property &amp; Capital Gains Tax Minimisation</li>
    <li class="service"><span class="service__icon"><i></i></span>Self-Managed Superannuation Funds (SMSF)</li>
    <li class="service"><span class="service__icon"><i></i></span>Small Business &amp; Personal Taxation</li>
    <li class="service"><span class="service__icon"><i></i></span>Investment Advice &amp; Risk Insurances</li>
  </ul>

  <svg class="abs" style="top:720px" width="400" height="104" viewBox="0 0 400 104">
    <path d="M0,44 Q200,-12 400,62 L400,104 L0,104 Z" fill="#2b2d2c"/>
    <path d="M48,30 Q210,-2 400,56" fill="none" stroke="#7dc242" stroke-width="7"/>
    <path d="M60,14 L22,40 L66,48 Z" fill="#7dc242"/>
  </svg>
  <div class="abs phone-line" style="top:770px;font-size:19px">
    <svg width="14" height="14" viewBox="0 0 24 24"><path d="M6.6 10.8a15 15 0 0 0 6.6 6.6l2.2-2.2a1 1 0 0 1 1-.25 11.4 11.4 0 0 0 3.6.6 1 1 0 0 1 1 1V20a1 1 0 0 1-1 1A17 17 0 0 1 3 4a1 1 0 0 1 1-1h3.5a1 1 0 0 1 1 1c0 1.25.2 2.45.6 3.6a1 1 0 0 1-.25 1z" fill="#7dc242"/></svg>
    (02) 4355 0182
  </div>
  <p class="abs center web" style="top:798px">www.beyondledger.com.au</p>
</section>

<!-- BACK -->
<section class="flyer flyer--back">
  <div class="abs" style="top:0;height:96px;background:var(--paper)"></div>
  <div class="brand" style="top:34px"><span class="brand__dot"></span><span class="brand__name" style="font-size:27px">Beyond The Ledger</span></div>
  <div class="photo photo--back" role="img" aria-label="Photo: cupped hands holding a small wooden house behind rising coin stacks with growing seedlings"></div>
  <svg class="abs" style="top:380px" width="400" height="100" viewBox="0 0 400 100">
    <path d="M0,38 Q200,-16 400,52 L400,100 L0,100 Z" fill="#2b2d2c"/>
    <path d="M50,22 Q230,-8 400,48" fill="none" stroke="#7dc242" stroke-width="7"/>
    <path d="M64,4 L26,28 L68,40 Z" fill="#7dc242"/>
  </svg>

  <p class="abs center advice" style="top:444px">ADVICE</p>
  <p class="abs center trust" style="top:488px">you can Trust</p>
  <p class="abs center lead" style="top:540px">Looking to Start or Grow your Business?</p>
  <p class="abs center contact" style="top:572px">Contact Us Today</p>

  <svg class="abs icon" style="top:607px;left:193px;width:14px" width="14" height="14" viewBox="0 0 24 24"><path d="M6.6 10.8a15 15 0 0 0 6.6 6.6l2.2-2.2a1 1 0 0 1 1-.25 11.4 11.4 0 0 0 3.6.6 1 1 0 0 1 1 1V20a1 1 0 0 1-1 1A17 17 0 0 1 3 4a1 1 0 0 1 1-1h3.5a1 1 0 0 1 1 1c0 1.25.2 2.45.6 3.6a1 1 0 0 1-.25 1z" fill="#7dc242"/></svg>
  <p class="abs center phone-line" style="top:623px;font-size:19px">(02) 4355 0182</p>

  <svg class="abs icon" style="top:652px;left:191px;width:18px" width="18" height="16" viewBox="0 0 24 20"><path d="M12 1 1 10h3v9h6v-6h4v6h6v-9h3z" fill="#7dc242"/></svg>
  <p class="abs center detail" style="top:670px">7 / 118 Harbourview Rd Erina NSW 2250<br>2 / 31 Lakeside Pde Toukley NSW 2263 (By Appointment)</p>

  <svg class="abs icon" style="top:706px;left:192px;width:16px" width="16" height="12" viewBox="0 0 24 18"><rect x="1" y="1" width="22" height="16" rx="1.5" fill="#7dc242"/><path d="M1.5 2 12 10 22.5 2" fill="none" stroke="#2b2d2c" stroke-width="2"/></svg>
  <p class="abs center detail" style="top:720px">info@beyondledger.com.au</p>

  <svg class="abs icon" style="top:742px;left:192px;width:16px" width="16" height="16" viewBox="0 0 24 24"><g fill="none" stroke="#7dc242" stroke-width="2"><circle cx="12" cy="12" r="10"/><ellipse cx="12" cy="12" rx="4.5" ry="10"/><path d="M2 12h20M4 6.5h16M4 17.5h16"/></g></svg>
  <p class="abs center web" style="top:760px">www.beyondledger.com.au</p>

  <div class="social">
    <span class="social__rule"></span>
    <span class="social__dot"></span><span class="social__dot"></span><span class="social__dot"></span><span class="social__dot"></span><span class="social__dot"></span>
    <span class="social__rule"></span>
  </div>
</section>

<p class="caption caption--front">FRONT</p>
<p class="caption caption--back">BACK</p>

</body>
</html>
```